Robotic Physical Therapy office needs a Grand Opening Flyer

We need a Grand Opening flyer design for a robotic physical therapy office named Kestrel Motion Therapy. We would like it to have a clean, classy, upscale feeling that gives potential clients a V.I.P. feeling. We would like to use the colors black, gray, and yellow (logo will be uploaded).

Event: Thursday, June 1st, 2023 from 12pm-6pm
location: 58240 Harlan Crest Ave, Pinegate Hollow, MI 48917

Industry/Entity Type

Physical therapy

Font styles to use
Script

Colors

Designer to choose colors to be used in the design.

Requirements
Nice to have
• More of a vip feel for the invite

```html
<!DOCTYPE html>
<html lang="en">
<head>
<meta charset="utf-8">
<title>Kestrel Motion Therapy – Grand Opening</title>
<link href="https://fonts.googleapis.com/css2?family=Poppins:wght@300;400;500;600;700;800&family=League+Spartan:wght@400;800&display=swap" rel="stylesheet">
<style>
  :root{
    --page:#dcdcdc;
    --ink:#111111;
    --black:#050505;
    --white:#ffffff;
    --yellow:#f6d92e;
    --gold:#d9a62a;
    --gold-light:#f3d36a;
    --rule:#8a8a8a;
    --muted:#2a2a2a;
  }
  *{margin:0;padding:0;box-sizing:border-box}
  html,body{width:1200px;height:1200px;overflow:hidden;background:var(--page)}
  body{position:relative;font-family:"Poppins",sans-serif;color:var(--ink)}
  .flyer{position:absolute;left:225px;top:68px;width:753px;height:1065px;background:var(--white);overflow:hidden}
  .flyer-art{position:absolute;inset:0}
  .abs{position:absolute;left:0;width:100%;text-align:center}

  .brand{top:108px;display:flex;justify-content:center;align-items:center;gap:12px}
  .brand-dot{width:46px;height:46px;border-radius:50%;background:var(--white)}
  .brand-name{font-family:"Poppins",sans-serif;font-weight:600;font-size:26px;line-height:1.05;color:var(--white);text-align:left;letter-spacing:.5px}

  .title-grand{top:200px;font-family:"Poppins",sans-serif;font-weight:700;font-size:144px;line-height:1;color:var(--yellow);letter-spacing:-2px}
  .title-opening{top:333px;font-family:"Poppins",sans-serif;font-weight:500;font-size:96px;line-height:1;color:var(--white);letter-spacing:-1px}
  .subtitle{top:449px;font-family:"Poppins",sans-serif;font-weight:400;font-size:25px;letter-spacing:.22em;color:var(--white)}

  .event-box{position:absolute;left:56px;top:720px;width:642px;height:103px;border:1px solid var(--rule);border-radius:10px}
  .event-label{top:707px;left:50%;width:auto;transform:translateX(-50%);background:var(--white);padding:0 8px;font-weight:400;font-size:22px;letter-spacing:.14em}
  .event-date{top:747px;font-family:"League Spartan",sans-serif;font-weight:800;font-size:41px;line-height:1;letter-spacing:-.3px}
  .event-date .year{font-weight:400}
  .event-time{position:absolute;left:155px;top:792px;width:443px;height:51px;border-radius:14px;background:var(--yellow);display:flex;align-items:center;justify-content:center;font-size:34px;letter-spacing:.04em;gap:12px}
  .event-time .from{font-weight:400}
  .event-time .hours{font-weight:700;font-family:"League Spartan",sans-serif;font-size:38px;padding-top:5px}

  .pin{position:absolute;left:353px;top:839px;width:48px;height:48px}
  .address{top:888px;font-weight:600;font-size:21px}
  .address-note{top:916px;font-weight:400;font-size:14px;line-height:17px;color:var(--muted)}
  .host{position:absolute;left:213px;top:962px;width:319px;height:25px;border:1px solid #9a9a9a;border-radius:6px;font-size:16px;line-height:23px;text-align:center}
  .host strong{font-weight:600}
  .rsvp{top:1000px;font-size:14px;font-weight:500}
  .rsvp strong{font-weight:700}
  .footer-band{position:absolute;left:0;bottom:0;width:100%;height:26px;background:var(--black)}
</style>
</head>
<body>
<main class="flyer">
  <svg class="flyer-art" width="753" height="1065" viewBox="0 0 753 1065">
    <defs>
      <radialGradient id="sparkleTone" cx="50%" cy="10%" r="90%">
        <stop offset="0" stop-color="#3a2a10"/>
        <stop offset=".35" stop-color="#0c0a07"/>
        <stop offset=".75" stop-color="#050505"/>
        <stop offset="1" stop-color="#3b3b3b"/>
      </radialGradient>
      <linearGradient id="ribbon" x1="0" y1="0" x2="1" y2="0">
        <stop offset="0" stop-color="#a9781a"/>
        <stop offset=".35" stop-color="#f3d36a"/>
        <stop offset=".65" stop-color="#b98a22"/>
        <stop offset="1" stop-color="#e9c25a"/>
      </linearGradient>
      <radialGradient id="scissorTone" cx="50%" cy="50%" r="50%">
        <stop offset="0" stop-color="#d6b04a" stop-opacity=".85"/>
        <stop offset=".7" stop-color="#c9c9c9" stop-opacity=".35"/>
        <stop offset="1" stop-color="#c9c9c9" stop-opacity="0"/>
      </radialGradient>
    </defs>
    <rect class="sparkle-backdrop" x="0" y="0" width="753" height="740" fill="url(#sparkleTone)" role="img" aria-label="Dark backdrop with golden bokeh lights and silver glitter"/>
    <path class="ribbon-band" d="M0,476 C70,520 120,640 230,640 C330,640 400,560 480,560 C600,560 640,700 753,700 L753,716 C640,716 600,596 480,596 C400,596 330,680 230,680 C110,680 60,560 0,500 Z" fill="url(#ribbon)"/>
    <path class="wave-edge" d="M0,500 C60,560 110,680 230,680 C330,680 400,596 480,596 C600,596 640,716 753,716 L753,1065 L0,1065 Z" fill="var(--black)"/>
    <path class="white-wave" d="M0,508 C60,568 110,688 230,688 C330,688 400,604 480,604 C600,604 640,724 753,724 L753,1065 L0,1065 Z" fill="var(--white)"/>
    <ellipse class="scissors-art" cx="356" cy="615" rx="135" ry="95" fill="url(#scissorTone)" role="img" aria-label="Gold scissors cutting the ribbon"/>
    <line x1="115" y1="435" x2="638" y2="435" stroke="#8c8c8c" stroke-width="1"/>
    <line x1="115" y1="489" x2="638" y2="489" stroke="#8c8c8c" stroke-width="1"/>
  </svg>

  <div class="abs brand">
    <span class="brand-dot"></span>
    <span class="brand-name">KESTREL MOTION<br>THERAPY</span>
  </div>

  <h1 class="abs title-grand">GRAND</h1>
  <h2 class="abs title-opening">OPENING</h2>
  <p class="abs subtitle">ROBOTIC PHYSICAL THERAPY</p>

  <div class="event-box"></div>
  <p class="abs event-label">EVENT</p>
  <p class="abs event-date">THURSDAY, JUNE 1ST, <span class="year">2023</span></p>
  <p class="event-time"><span class="from">FROM</span><span class="hours">12PM-6PM</span></p>

  <svg class="pin" viewBox="0 0 48 48" aria-hidden="true">
    <circle cx="24" cy="24" r="23" fill="var(--white)"/>
    <circle cx="24" cy="24" r="21" fill="var(--ink)"/>
    <path d="M24 13c-5 0-8.5 3.6-8.5 8.3 0 5.8 8.5 14 8.5 14s8.5-8.2 8.5-14C32.5 16.6 29 13 24 13z" fill="var(--yellow)"/>
    <circle cx="24" cy="21.5" r="3.2" fill="var(--ink)"/>
  </svg>

  <p class="abs address">58240 Harlan Crest Ave, Pinegate Hollow, MI 48917</p>
  <p class="abs address-note">(Located in the Larchmont Commons Shopping Center on<br>Harlan Crest Ave, North of Birchfield Rd.)</p>
  <p class="host">Hosted by <strong>Daniel and Mira Castell</strong></p>
  <p class="abs rsvp"><strong>Please text RSVP to :</strong> 555-014-2287</p>
  <div class="footer-band"></div>
</main>
</body>
</html>
```